Vantrel Ashcombe LLC

we need a business card design

Industry/Entity Type

hvac

Contact Information for Business Card

my logo

Requirements
Must have
• my logo and same colors

```html
<!DOCTYPE html>
<html lang="en">
<head>
<meta charset="utf-8">
<title>Vantrel Ashcombe LLC – Business Card</title>
<link rel="stylesheet" href="https://fonts.googleapis.com/css2?family=Poppins:wght@500;600;700&family=Oswald:wght@600&display=swap">
<style>
  :root {
    --backdrop: #d4d5d7;
    --card-blue-deep: #0a56a0;
    --card-blue-light: #0d6cb4;
    --accent-orange: #f5aa3c;
    --text-white: #ffffff;
  }
  * { box-sizing: border-box; margin: 0; padding: 0; }
  html, body { width: 900px; height: 1200px; overflow: hidden; }
  body { background: var(--backdrop); position: relative; font-family: "Poppins", sans-serif; }

  .card {
    position: absolute;
    left: 135px;
    width: 630px;
    height: 357px;
    background: linear-gradient(135deg, var(--card-blue-deep) 0%, var(--card-blue-light) 100%);
    color: var(--text-white);
  }
  .card--front { top: 214px; }
  .card--back { top: 628px; background: linear-gradient(160deg, var(--card-blue-light) 0%, var(--card-blue-deep) 100%); }

  .brand {
    position: absolute;
    display: flex;
    align-items: center;
    gap: 12px;
    transform: translate(-50%, -50%);
    white-space: nowrap;
  }
  .brand__dot { width: 22px; height: 22px; border-radius: 50%; background: var(--accent-orange); flex: none; }
  .brand__name { font-weight: 700; color: var(--text-white); }
  .card--front .brand { left: 315px; top: 179px; }
  .card--front .brand__name { font-size: 34px; }
  .card--back .brand { left: 457px; top: 111px; }
  .card--back .brand__name { font-size: 24px; }

  .offer-line {
    position: absolute;
    left: 0; right: 0; top: 314px;
    text-align: center;
    font-family: "Oswald", sans-serif;
    font-weight: 600;
    font-size: 12.5px;
    letter-spacing: 0.1px;
    text-transform: uppercase;
  }

  .contact-block { position: absolute; left: 39px; top: 170px; }
  .contact-block__name {
    font-weight: 700; font-size: 23px; color: var(--accent-orange);
    text-transform: uppercase; line-height: 1.1;
  }
  .contact-block__role { font-weight: 500; font-size: 14px; margin-top: 2px; }
  .contact-block__rule { width: 48px; height: 3px; background: var(--accent-orange); margin-top: 8px; }
  .contact-list { list-style: none; margin-top: 16px; }
  .contact-list__item {
    display: flex; align-items: center; gap: 9px;
    font-weight: 500; font-size: 14.5px; height: 28px;
  }
  .contact-list__item--phone { letter-spacing: 2.5px; }
  .contact-list__icon { width: 14px; height: 14px; flex: none; }
</style>
</head>
<body>
  <section class="card card--front">
    <div class="brand">
      <span class="brand__dot"></span>
      <span class="brand__name">Vantrel Ashcombe LLC</span>
    </div>
    <p class="offer-line">Free AC service calls with repairs - same day AC repairs, next day air conditioning installation</p>
  </section>

  <section class="card card--back">
    <div class="brand">
      <span class="brand__dot"></span>
      <span class="brand__name">Vantrel Ashcombe LLC</span>
    </div>
    <div class="contact-block">
      <h1 class="contact-block__name">Dorian Pelham</h1>
      <p class="contact-block__role">Owner</p>
      <div class="contact-block__rule"></div>
      <ul class="contact-list">
        <li class="contact-list__item contact-list__item--phone">
          <svg class="contact-list__icon" viewBox="0 0 24 24"><path fill="#f5aa3c" d="M6.6 10.8a15.1 15.1 0 0 0 6.6 6.6l2.2-2.2a1 1 0 0 1 1-.25 11.4 11.4 0 0 0 3.6.57 1 1 0 0 1 1 1V20a1 1 0 0 1-1 1A17 17 0 0 1 3 4a1 1 0 0 1 1-1h3.5a1 1 0 0 1 1 1c0 1.25.2 2.45.57 3.57a1 1 0 0 1-.25 1z"/></svg>
          555-014-2273
        </li>
        <li class="contact-list__item">
          <svg class="contact-list__icon" viewBox="0 0 24 24"><rect x="2" y="5" width="20" height="14" fill="#f5aa3c"/><path d="M2 5l10 8 10-8" fill="none" stroke="#0a5ca6" stroke-width="2"/></svg>
          dorian@vantrelashcombe.com
        </li>
        <li class="contact-list__item">
          <svg class="contact-list__icon" viewBox="0 0 24 24" fill="none" stroke="#f5aa3c" stroke-width="2"><circle cx="12" cy="12" r="10"/><ellipse cx="12" cy="12" rx="4" ry="10"/><path d="M2 12h20M4 7h16M4 17h16"/></svg>
          vantrelashcombe.com
        </li>
      </ul>
    </div>
  </section>
</body>
</html>
```